Criação de Peça Gráfica (unidade) para Logística, Entrega & Armazenamento
A empresa queria:
" Transporte Geral de Cargas, seja rodoviário, rodo-fluvial e maritímo. Também somos Agentes/Representantes Internacioais "

```html
<!DOCTYPE html>
<html lang="pt-BR">
<head>
<meta charset="utf-8">
<title>Serviços Nacionais</title>
<link href="https://fonts.googleapis.com/css2?family=Arimo:wght@400;700&display=swap" rel="stylesheet">
<style>
  :root {
    --page-bg: #eeeeee;
    --slide-bg: #ffffff;
    --brand-red: #7b1a24;
    --bullet-red: #8c1c27;
    --text-dark: #333333;
    --haze-1: #f7f8f9;
    --haze-2: #e6e9ec;
  }
  * { box-sizing: border-box; margin: 0; padding: 0; }
  html, body {
    width: 1200px; height: 1200px; overflow: hidden;
    background: var(--page-bg);
    font-family: "Arimo", Arial, sans-serif;
    color: var(--text-dark);
  }
  .slide {
    position: absolute; left: 141px; top: 319px;
    width: 918px; height: 562px;
    background: var(--slide-bg);
    overflow: hidden;
  }
  .slide-backdrop {
    position: absolute; inset: 0 0 34% 0;
    background: linear-gradient(100deg, var(--haze-1) 0%, #ffffff 40%, var(--haze-2) 75%, var(--haze-1) 100%);
  }
  .title {
    position: absolute; left: 6.5%; top: 16.5%;
    font-size: 26px; font-weight: 700; color: var(--brand-red);
    letter-spacing: 0.2px;
  }
  .title-rule {
    position: absolute; left: 0; top: 23.5%;
    width: 43%; height: 2px; background: var(--brand-red);
  }
  .brand-name {
    position: absolute; right: 3%; top: 12%;
    font-size: 11px; font-weight: 400; color: var(--text-dark);
    letter-spacing: 0.5px;
  }
  .service {
    position: absolute; font-size: 12px; line-height: 1.6;
  }
  .service-left { left: 14%; top: 31%; }
  .service-right { left: 46.5%; top: 31%; }
  .service-head { display: flex; align-items: flex-start; gap: 10px; }
  .tick { width: 10px; height: 10px; margin-top: 4px; flex: none; }
  .service-intro { margin-left: 20px; }
  .items { list-style: none; margin-top: 22px; margin-left: 20px; }
  .service-right .items { margin-top: 2px; margin-left: 20px; }
  .items li { position: relative; padding-left: 18px; line-height: 1.6; }
  .items li::before {
    content: ""; position: absolute; left: 0; top: 7px;
    width: 4px; height: 4px; background: var(--bullet-red);
  }
  .photo-strip {
    position: absolute; left: 0; right: 0; bottom: 0; height: 34%;
    display: flex; gap: 3px; background: #ffffff;
  }
  .photo { height: 100%; }
  .photo-truck { width: 23.5%; background: linear-gradient(180deg, #e9b98a 0%, #b98a68 55%, #4d4a4a 100%); }
  .photo-ship { width: 25.6%; background: linear-gradient(180deg, #c9d3dc 0%, #9a6a5e 50%, #1f6a78 100%); }
  .photo-plane { width: 24.8%; background: linear-gradient(180deg, #5f9fd6 0%, #8fc1e6 55%, #2a6aa5 100%); }
  .photo-cargo { flex: 1; background: linear-gradient(180deg, #dce6ef 0%, #a8b7c6 50%, #9c8466 100%); }
</style>
</head>
<body>
  <section class="slide">
    <div class="slide-backdrop" role="img" aria-label="Fundo suave com avião e navio em tons de cinza claro"></div>

    <h1 class="title">SERVIÇOS NACIONAIS</h1>
    <div class="title-rule"></div>

    <div class="brand-name">NORTEMAR LOG</div>

    <div class="service service-left">
      <div class="service-head">
        <svg class="tick" viewBox="0 0 12 12"><path d="M1 6.5 L4.5 10 L11 2" fill="none" stroke="#8c1c27" stroke-width="1.8"/></svg>
        <span>Transporte RODOVIÁRIO e CABOTAGEM:</span>
      </div>
      <ul class="items">
        <li>Cargas secas;</li>
        <li>Fracionada ou lotação;</li>
        <li>Manuseio de carga;</li>
        <li>Coleta e Distribuição;</li>
      </ul>
    </div>

    <div class="service service-right">
      <div class="service-head">
        <svg class="tick" viewBox="0 0 12 12"><path d="M1 6.5 L4.5 10 L11 2" fill="none" stroke="#8c1c27" stroke-width="1.8"/></svg>
        <span>Transporte AÉREO:</span>
      </div>
      <p class="service-intro">Operando no agenciamento de cargas com os serviços de:</p>
      <ul class="items">
        <li>Coleta e Distribuição;</li>
        <li>Manuseio de carga;</li>
      </ul>
    </div>

    <div class="photo-strip">
      <div class="photo photo-truck" role="img" aria-label="Foto de caminhão na estrada ao pôr do sol"></div>
      <div class="photo photo-ship" role="img" aria-label="Foto de navio porta-contêineres no porto"></div>
      <div class="photo photo-plane" role="img" aria-label="Foto de avião de carga no céu azul"></div>
      <div class="photo photo-cargo" role="img" aria-label="Foto de avião, caminhão e cargas paletizadas"></div>
    </div>
  </section>
</body>
</html>
```